Need help in designing new business card utilizing our new logo.

BuildMarq Solutions works with Construction Business Owners, Managers & IT Professionals to strengthen software usage and increase user productivity.

Our Construction Accounting and Mobile Field Management Software Clients engage with us in the following areas:

New Software Implementations
Software Re-Implementations
Redesigning Software Usage at the User Level
Project Coordination & Management
Continued Software Support

Old tag line:
Weighing Options - Implementing Solutions

www.buildmarq-solutions.example

Stride 4 is a product, but not needed for a new business card.

```html
<!DOCTYPE html>
<html lang="en">
<head>
<meta charset="utf-8">
<title>BuildMarq Solutions – Business Card</title>
<link href="https://fonts.googleapis.com/css2?family=Montserrat:wght@600&family=Oswald:wght@600&family=Jost:wght@400;500;600&display=swap" rel="stylesheet">
<style>
  :root{
    --stage:#2e2e2e;
    --card:#ffffff;
    --brand-blue:#2e3192;
    --ink:#2b2b2b;
    --rule:#1f1f1f;
    --stripe-grey:#5a5a5a;
    --map-grey:#e2e2e2;
    --map-grey-soft:#eeeeee;
  }
  *{margin:0;padding:0;box-sizing:border-box}
  html,body{width:1200px;height:899px;overflow:hidden;background:var(--stage)}
  .stage{position:relative;width:1200px;height:899px}
  .card{position:absolute;left:250px;width:700px;height:400px;background:var(--card);overflow:hidden;
        box-shadow:0 10px 24px rgba(0,0,0,.45)}
  .card--front{top:30px}
  .card--back{top:469px}

  /* brand lockup */
  .brand{position:absolute;display:flex;align-items:center;gap:14px}
  .brand__mark{width:44px;height:44px;background:var(--brand-blue)}
  .brand__divider{width:3px;height:70px;background:var(--brand-blue)}
  .brand__name{font-family:"Montserrat",sans-serif;font-weight:600;color:var(--brand-blue);font-size:34px;letter-spacing:.5px;white-space:nowrap}

  /* front */
  .world-map{position:absolute;left:90px;top:25px;width:590px;height:330px;border-radius:40px;
             background:radial-gradient(ellipse at 50% 45%,var(--map-grey) 0%,var(--map-grey-soft) 60%,#f8f8f8 100%)}
  .card--front .brand{left:150px;top:140px}
  .front__web{position:absolute;left:0;right:0;bottom:22px;text-align:center;font-family:"Jost",sans-serif;font-weight:500;
              font-size:17px;color:var(--brand-blue);letter-spacing:.6px}

  /* back */
  .card--back .brand{left:40px;top:38px}
  .card--back .brand__name{font-size:30px}
  .back__rule{position:absolute;left:50px;top:188px;width:560px;height:2px;background:var(--rule)}
  .contact{position:absolute;left:48px;top:210px;list-style:none;font-family:"Jost",sans-serif;font-size:17px;color:var(--ink)}
  .contact li{display:flex;align-items:center;gap:10px;height:26px}
  .contact svg{width:16px;height:16px;fill:var(--brand-blue);flex:none}
  .contact .ext{font-size:14px}
  .contact .web b{font-weight:600;color:var(--brand-blue)}
  .person{position:absolute;right:40px;top:200px;text-align:right}
  .person__name{font-family:"Oswald",sans-serif;font-weight:600;font-size:34px;color:var(--ink);letter-spacing:.5px;line-height:1.1}
  .person__role{font-family:"Montserrat",sans-serif;font-weight:600;font-size:16px;color:var(--ink)}
  .address{position:absolute;right:40px;top:290px;text-align:right;font-family:"Jost",sans-serif;font-size:17px;color:var(--ink);line-height:1.4}
  .back__band{position:absolute;left:0;top:0;width:700px;height:400px}
</style>
</head>
<body>
<main class="stage">

  <section class="card card--front">
    <div class="world-map" role="img" aria-label="Light grey world map in the background"></div>
    <div class="brand">
      <span class="brand__mark"></span>
      <span class="brand__divider"></span>
      <span class="brand__name">BuildMarq Solutions</span>
    </div>
    <p class="front__web">www.buildmarq-solutions.example</p>
  </section>

  <section class="card card--back">
    <svg class="back__band" viewBox="0 0 700 400" aria-hidden="true">
      <path d="M0 350 L420 350 C440 350 445 362 462 362" fill="none" stroke="#5a5a5a" stroke-width="4"/>
      <path d="M0 362 L440 362 C470 362 470 346 500 346 L700 346 L700 400 L0 400 Z" fill="#2e3192"/>
      <rect x="688" y="228" width="20" height="50" rx="6" fill="#2e3192"/>
    </svg>

    <div class="brand">
      <span class="brand__mark"></span>
      <span class="brand__divider"></span>
      <span class="brand__name">BuildMarq Solutions</span>
    </div>

    <div class="back__rule"></div>

    <ul class="contact">
      <li><svg viewBox="0 0 16 16"><path d="M3 1l3 3-1.5 2a9 9 0 005.5 5.5L12 10l3 3-2 2C6 15 1 10 1 3z"/></svg>800-555-0142 <span class="ext">ext.100</span></li>
      <li><svg viewBox="0 0 16 16"><path d="M4 0h8a1 1 0 011 1v14a1 1 0 01-1 1H4a1 1 0 01-1-1V1a1 1 0 011-1zm1 2v10h6V2zm3 11a1 1 0 100 2 1 1 0 000-2z"/></svg>518-555-0187</li>
      <li><svg viewBox="0 0 16 16"><path d="M0 3h16v1L8 9 0 4zm0 3l8 5 8-5v7H0z"/></svg>dana.whitfield@buildmarq-solutions.example</li>
      <li class="web"><svg viewBox="0 0 16 16"><path d="M10 1a5 5 0 110 10 5 5 0 010-10zm0 2a3 3 0 100 6 3 3 0 000-6zM5.5 9.5l1.4 1.4L2 15.8.6 14.4z"/></svg>www.<b>buildmarq-solutions</b>.example</li>
    </ul>

    <div class="person">
      <p class="person__name">DANA R. WHITFIELD</p>
      <p class="person__role">Owner</p>
    </div>

    <p class="address">48 Linden Avenue - Suite 210<br>Millbrook NY 12545</p>
  </section>

</main>
</body>
</html>
```